Local Flower Farm Needs Business Card Design

I need business cards designed for a flower farm based in Eudora, Kansas.
Business Info:
We are a local cut flower farm located in Eudora, Kansas, founded by Darla Hoffstrom. What started as a passion for agriculture and search for more joy in daily life has blossomed into a small business dedicated to providing the community with beautiful, fresh, and sustainable flowers. We specialize in local, seasonal blooms, ensuring that every petal reflects the care and dedication we pour into our craft. Our mission is to deliver the highest quality flowers directly to our customers through local farmers markets and to florists who share our commitment to sustainability. Join us in celebrating the beauty of nature, one bloom at a time!
Contact Details:
Darla Hoffstrom
Owner
Phone 913-555-0147
Facebook: Lorabelle Quinn Blossoms
Instagram: @LorabelleQuinnBlossoms
Website: LorabelleQuinnBlossoms.example
Target Market(s)
Wholesale to Florists and Direct to Consumer via Farmers Market
Industry/Entity Type
Florist, Farm
Contact Information for Business Card
Name, Contact Info, Logo
Look and feel

```html
<!DOCTYPE html>
<html lang="en">
<head>
<meta charset="utf-8">
<title>Lorabelle Quinn Blossoms – Business Cards</title>
<link href="https://fonts.googleapis.com/css2?family=Tinos:wght@400;700&display=swap" rel="stylesheet">
<style>
  :root {
    --stage: #15171a;
    --card-deep: #08191d;
    --card-mid: #0c2a30;
    --card-teal: #124049;
    --glow: rgba(52,118,126,0.55);
    --glow-soft: rgba(30,84,92,0.35);
    --ink: #ffffff;
    --rule: rgba(255,255,255,0.85);
  }
  * { margin: 0; padding: 0; box-sizing: border-box; }
  html, body { width: 1200px; height: 840px; overflow: hidden; }
  body {
    background: var(--stage);
    font-family: "Tinos", "Times New Roman", serif;
    color: var(--ink);
    position: relative;
  }
  .card {
    position: absolute;
    width: 560px;
    height: 320px;
    border-radius: 26px;
    overflow: hidden;
  }
  .card--front {
    left: 80px; top: 70px;
    background: linear-gradient(120deg, var(--card-mid) 0%, var(--card-deep) 55%, var(--card-mid) 100%);
  }
  .card--back {
    left: 560px; top: 450px;
    background: linear-gradient(135deg, var(--card-teal) 0%, var(--card-deep) 45%, var(--card-mid) 100%);
  }

  /* Front: soft tonal glow where the embossed floral decoration sits */
  .front-decor {
    position: absolute;
    left: 250px; top: -40px;
    width: 340px; height: 400px;
    background:
      radial-gradient(ellipse 45% 40% at 68% 62%, var(--glow) 0%, rgba(18,64,73,0) 100%),
      radial-gradient(ellipse 55% 55% at 55% 35%, var(--glow-soft) 0%, rgba(18,64,73,0) 100%);
  }

  .brand-seal {
    position: absolute;
    border: 1.5px solid var(--ink);
    border-radius: 50%;
    display: flex;
    align-items: center;
    justify-content: center;
    text-align: center;
    z-index: 1;
  }
  .brand-seal__name {
    font-weight: 400;
    letter-spacing: 0.12em;
    text-transform: uppercase;
    line-height: 1.3;
  }
  .card--front .brand-seal { left: 70px; top: 65px; width: 190px; height: 190px; }
  .card--front .brand-seal__name { font-size: 18px; }

  .card--back .brand-seal { right: 50px; top: 42px; width: 150px; height: 150px; }
  .card--back .brand-seal__name { font-size: 13px; }

  .holder__name {
    position: absolute;
    left: 36px; top: 184px;
    font-weight: 700; font-size: 24px; letter-spacing: 0.03em;
    text-transform: uppercase; line-height: 1;
  }
  .top-rule {
    position: absolute;
    left: 36px; right: 26px; top: 214px;
    border-top: 1px solid var(--rule);
  }
  .holder__role {
    position: absolute;
    left: 50px; top: 218px;
    font-size: 15px; line-height: 1.2;
  }
  .holder-rule {
    position: absolute;
    left: 50px; width: 230px; top: 242px;
    border-top: 1px solid var(--rule);
  }
  .contact { position: absolute; list-style: none; font-size: 15px; line-height: 1.2; }
  .contact li { display: flex; align-items: center; gap: 7px; margin-bottom: 5px; white-space: nowrap; }
  .contact--primary { left: 50px; top: 254px; }
  .contact--social { left: 320px; top: 226px; }
  .contact svg { flex: none; }
  .marker-square { width: 12px; height: 12px; background: var(--ink); border-radius: 2px; flex: none; }
  .marker-circle { width: 12px; height: 12px; border: 1.5px solid var(--ink); border-radius: 50%; flex: none; }
</style>
</head>
<body>

<section class="card card--front" aria-label="Card front">
  <div class="front-decor" role="img" aria-label="Soft tonal embossed floral decoration"></div>
  <div class="brand-seal"><span class="brand-seal__name">Lorabelle<br>Quinn<br>Blossoms</span></div>
</section>

<section class="card card--back" aria-label="Card back">
  <div class="brand-seal"><span class="brand-seal__name">Lorabelle<br>Quinn<br>Blossoms</span></div>

  <p class="holder__name">Darla Hoffstrom</p>
  <div class="top-rule"></div>
  <p class="holder__role">Owner</p>
  <div class="holder-rule"></div>

  <ul class="contact contact--primary">
    <li>
      <svg width="14" height="14" viewBox="0 0 24 24" aria-hidden="true"><path fill="#fff" d="M6.6 10.8a15 15 0 0 0 6.6 6.6l2.2-2.2a1 1 0 0 1 1-.25 11.4 11.4 0 0 0 3.6.57 1 1 0 0 1 1 1V20a1 1 0 0 1-1 1A17 17 0 0 1 3 4a1 1 0 0 1 1-1h3.5a1 1 0 0 1 1 1c0 1.250.2 2.45.57 3.57a1 1 0 0 1-.25 1z"/></svg>
      913-555-0147
    </li>
    <li>
      <svg width="14" height="14" viewBox="0 0 24 24" aria-hidden="true"><circle cx="12" cy="12" r="10" fill="none" stroke="#fff" stroke-width="2"/><ellipse cx="12" cy="12" rx="4" ry="10" fill="none" stroke="#fff" stroke-width="1.5"/><line x1="2" y1="12" x2="22" y2="12" stroke="#fff" stroke-width="1.5"/></svg>
      LorabelleQuinnBlossoms.example
    </li>
  </ul>

  <ul class="contact contact--social">
    <li><span class="marker-square"></span>Lorabelle Quinn Blossoms</li>
    <li><span class="marker-circle"></span>@LorabelleQuinnBlossoms</li>
  </ul>
</section>

</body>
</html>
```